Child care/Preparatory Business Card Design & logo design

I need a logo to use on a business card, letterhead, uniform and promotional material for a new business called 'Corella Kinderschool'. It is located in the north west of Western Australia in the Pilbara region. The service will provide a 'Steps Toward Schooling' program for 3 and 4 year old children. I would like a logo that shows unity, or belonging in children. I like the colour blue, any primary colours would be suitable. The design needs to be cheerful and appealing to children whilst still having an 'elite' edge to it.

Target Market(s)

Families with young children

Industry/Entity Type

Business

Contact Information for Business Card

Maren Tolling Director
Corella Kinderschool
M 0400 318 926
office@corellakinder.com.au
PO Box 591 Tarrowell WA 6735

Steps Toward Schooling

```html
<!DOCTYPE html>
<html lang="en">
<head>
<meta charset="utf-8">
<title>Corella Kinderschool – Business Card</title>
<link href="https://fonts.googleapis.com/css2?family=Poiret+One&display=swap" rel="stylesheet">
<style>
  :root {
    --card-bg: #ffffff;
    --brand-blue: #3a98c0;
    --text-blue: #2fa8dc;
    --accent-blue: #4a8fce;
  }
  * { margin: 0; padding: 0; box-sizing: border-box; }
  html, body {
    width: 1200px;
    height: 695px;
    overflow: hidden;
    background: var(--card-bg);
  }
  .card {
    position: relative;
    width: 1200px;
    height: 695px;
    background: var(--card-bg);
    font-family: "Poiret One", sans-serif;
    color: var(--text-blue);
  }
  .brand-mark {
    position: absolute;
    left: 510px;
    top: 110px;
    width: 180px;
    height: 180px;
  }
  .brand-name {
    position: absolute;
    left: 0;
    right: 0;
    top: 330px;
    text-align: center;
    font-size: 48px;
    font-weight: 400;
    line-height: 1;
    color: var(--brand-blue);
    white-space: nowrap;
  }
  .tagline {
    position: absolute;
    left: 0;
    right: 0;
    top: 390px;
    text-align: center;
    font-size: 40px;
    line-height: 1;
    white-space: nowrap;
  }
  .contact {
    position: absolute;
    top: 506px;
    font-size: 35px;
    line-height: 52px;
    white-space: nowrap;
  }
  .contact-left { left: 70px; text-align: left; }
  .contact-right { right: 63px; text-align: right; }
</style>
</head>
<body>
  <main class="card">
    <svg class="brand-mark" viewBox="0 0 180 180" aria-hidden="true">
      <rect x="0" y="0" width="180" height="180" fill="var(--accent-blue)"/>
    </svg>
    <h1 class="brand-name">Corella Kinderschool</h1>
    <p class="tagline">Steps Toward Schooling</p>

    <div class="contact contact-left">
      <p class="contact-name">Director Maren Tolling</p>
      <p class="contact-email">office@corellakinder.com.au</p>
    </div>
    <div class="contact contact-right">
      <p class="contact-phone">M 0400 318 926</p>
      <p class="contact-address">PO Box 591 Tarrowell WA 6735</p>
    </div>
  </main>
</body>
</html>
```